Letterhead for Law Firm - Logo already prepared

I previously used to prepare a logo which I was quite pleased with, a copy is attached for your reference. I would like the font of the logo to be all the same size, rather than the 'S' and 'L' being larger than the other letters.
I have copies of the attached in other formats if necessary.
I need a letterhead prepared which is virtually identical to the draft attached, however I will be adding an address, phone number, fax number, mobile number and email. I will provide these details with whoever can assist me.
I will also be providing insurance details to be listed at the foot of the page.
Finally, I need the file to be supplied as a high resolution pdf with 2mm bleed.
If you require any further information, please do not hesitate to contact me.

```html
<!DOCTYPE html>
<html lang="en">
<head>
<meta charset="utf-8">
<title>Marlowe Legal – Letterhead</title>
<link rel="stylesheet" href="https://fonts.googleapis.com/css2?family=Cinzel:wght@500&family=Open+Sans:wght@300;400;700&display=swap">
<style>
  :root {
    --paper: #ffffff;
    --paper-edge: #e9e9e9;
    --brand-orange: #f26a1b;
    --brand-orange-light: #f7931e;
    --brand-orange-deep: #e8541a;
    --tab-rim: #3b3b3b;
    --ink: #1d1d1d;
    --muted: #9a9a9a;
    --white: #ffffff;
  }
  * { box-sizing: border-box; margin: 0; padding: 0; }
  html, body {
    width: 948px;
    height: 1200px;
    overflow: hidden;
    background: var(--paper);
  }
  .letterhead {
    position: relative;
    width: 948px;
    height: 1200px;
    background: radial-gradient(ellipse at 50% 45%, var(--paper) 55%, var(--paper-edge) 100%);
    overflow: hidden;
  }
  .brand {
    position: absolute;
    left: 64px;
    top: 64px;
    display: flex;
    align-items: center;
    gap: 22px;
  }
  .brand-dot {
    width: 100px;
    height: 100px;
    border-radius: 50%;
    background: var(--brand-orange);
  }
  .brand-name {
    font-family: "Cinzel", serif;
    font-weight: 500;
    font-size: 44px;
    letter-spacing: 1px;
    color: var(--ink);
  }
  .insurance {
    position: absolute;
    left: 75px;
    top: 1124px;
    width: 590px;
    display: flex;
    align-items: baseline;
    font-family: "Open Sans", sans-serif;
    font-weight: 300;
    font-size: 24px;
    color: var(--muted);
  }
  .insurance-rule {
    flex: 1;
    margin-left: 4px;
    border-bottom: 2px dotted var(--muted);
  }
  .contact-tab {
    position: absolute;
    left: 0;
    top: 0;
    width: 948px;
    height: 1200px;
  }
  .tab-name {
    position: absolute;
    left: 700px;
    top: 966px;
    width: 150px;
    text-align: center;
    font-family: "Cinzel", serif;
    font-weight: 500;
    font-size: 20px;
    line-height: 1.1;
    color: var(--white);
  }
  .contact-list {
    position: absolute;
    left: 700px;
    top: 1060px;
    list-style: none;
    font-family: "Open Sans", sans-serif;
    font-size: 14px;
    color: var(--white);
  }
  .contact-list li {
    display: flex;
    align-items: center;
    gap: 8px;
    height: 18.5px;
  }
  .contact-list svg { width: 13px; height: 13px; flex: none; }
  .contact-list .web { font-weight: 700; }
</style>
</head>
<body>
<main class="letterhead">
  <header class="brand">
    <span class="brand-dot"></span>
    <span class="brand-name">Marlowe Legal</span>
  </header>

  <div class="insurance">
    <span>insurance details</span>
    <span class="insurance-rule"></span>
  </div>

  <svg class="contact-tab" viewBox="0 0 948 1200" aria-hidden="true">
    <defs>
      <linearGradient id="tabFill" x1="0" y1="0" x2="1" y2="1">
        <stop offset="0" stop-color="var(--brand-orange-deep)"/>
        <stop offset="0.6" stop-color="var(--brand-orange)"/>
        <stop offset="1" stop-color="var(--brand-orange-light)"/>
      </linearGradient>
    </defs>
    <path fill="var(--tab-rim)" d="M690 1200 L632 1060 Q620 1030 645 1008 L730 920 Q745 904 770 904 L890 904 Q935 904 948 950 L948 1200 Z"/>
    <path fill="url(#tabFill)" d="M690 1200 L632 1060 Q620 1030 645 1008 L728 926 Q743 911 768 911 L886 911 Q925 911 940 955 L940 1200 Z"/>
  </svg>

  <div class="tab-name">Marlowe<br>Legal</div>

  <ul class="contact-list">
    <li>
      <svg viewBox="0 0 16 16"><path fill="#fff" d="M3 1l3 3-1.5 2a8 8 0 0 0 5.5 5.5L12 10l3 3-2 2C7 15 1 9 1 3z"/></svg>
      <span>55-0142-3378</span>
    </li>
    <li>
      <svg viewBox="0 0 16 16"><rect x="2" y="6" width="12" height="8" fill="#fff"/><rect x="4" y="1" width="8" height="5" fill="none" stroke="#fff" stroke-width="1.5"/></svg>
      <span>55-0142-3379</span>
    </li>
    <li>
      <svg viewBox="0 0 16 16"><rect x="4" y="1" width="8" height="14" rx="1.5" fill="#fff"/><rect x="5.5" y="3" width="5" height="8" fill="var(--brand-orange)"/></svg>
      <span>55-0142-3380</span>
    </li>
    <li>
      <svg viewBox="0 0 16 16"><rect x="1" y="3" width="14" height="10" fill="#fff"/><path d="M1 3l7 6 7-6" fill="none" stroke="var(--brand-orange)" stroke-width="1.2"/></svg>
      <span>name@marlowelegal.com</span>
    </li>
    <li>
      <svg viewBox="0 0 16 16"><circle cx="8" cy="8" r="6.5" fill="none" stroke="#fff" stroke-width="1.5"/><ellipse cx="8" cy="8" rx="2.8" ry="6.5" fill="none" stroke="#fff" stroke-width="1.2"/><path d="M1.5 8h13" stroke="#fff" stroke-width="1.2"/></svg>
      <span class="web">www.marlowelegal.com</span>
    </li>
  </ul>
</main>
</body>
</html>
```